Property Service business needs a cool business card

Looking for an eloquent and unique business card using the logo and colours attached as uploaded files.

Target Market(s)

Body corporates, real estate agents, building managers

Industry/Entity Type

Business

Contact Information for Business Card

- Quorvel Logo
- Construction * Maintenance * Remedial

- Tom Wexley
- Business Manager

- Ph 0417586204
- P.O Box 461 South Melbourne Vic 3090
- Email tom@quorvel.com
- Website www.quorvelpropertyservices.com.au

Requirements
Must have
• Clean and fresh look, colours must be vibrant!
Nice to have
• unique features
Should not have
• Should not be overcrowded

```html
<!DOCTYPE html>
<html lang="en">
<head>
<meta charset="utf-8">
<title>Quorvel Property Services – Business Card</title>
<link rel="stylesheet" href="https://fonts.googleapis.com/css2?family=Open+Sans:wght@400;600;700&family=Roboto:wght@500&display=swap">
<style>
  :root {
    --backdrop-light: #c3ced6;
    --backdrop-dark: #8c9dab;
    --card-glass: #e3eaef;
    --card-glass-edge: #f4f7f9;
    --band-dark: #26292d;
    --band-darker: #1b1d20;
    --brand-blue: #1d5aa6;
    --brand-blue-bright: #1f63bd;
    --brand-blue-faint: #a9c0dc;
    --brand-green: #8cc63f;
    --brand-green-faint: #cfe5b4;
    --text-light: #f2f4f5;
    --divider: #8a8f94;
  }
  * { box-sizing: border-box; margin: 0; padding: 0; }
  html, body { width: 1200px; height: 792px; overflow: hidden; }
  body {
    background: radial-gradient(ellipse at 50% 45%, var(--backdrop-light) 0%, var(--backdrop-dark) 100%);
    position: relative;
    font-family: "Open Sans", Arial, sans-serif;
  }
  .card {
    position: absolute;
    top: 232px;
    width: 523px;
    height: 334px;
    border-radius: 18px;
    overflow: hidden;
    background: linear-gradient(180deg, var(--card-glass-edge) 0%, var(--card-glass) 100%);
    box-shadow: 0 0 0 1px rgba(255,255,255,0.6);
  }
  .card--front { left: 55px; }
  .card--back { left: 624px; }
  .card__stripe {
    position: absolute; left: 0; right: 0; top: 183px; height: 10px;
    background: var(--brand-blue);
  }
  .card__band {
    position: absolute; left: 0; right: 0; top: 193px; bottom: 0;
    background: linear-gradient(180deg, var(--band-dark) 0%, var(--band-darker) 100%);
  }
  .brand {
    position: absolute; top: 62px; left: 88px;
    display: flex; align-items: center; gap: 22px;
  }
  .brand__square {
    width: 62px; height: 62px; background: var(--brand-green);
  }
  .brand__name {
    font-family: "Open Sans", Arial, sans-serif;
    font-weight: 600;
    font-size: 48px; line-height: 1; color: var(--brand-blue);
  }
  .brand--faint { left: auto; right: 84px; }
  .brand--faint .brand__square { background: var(--brand-green-faint); }
  .brand--faint .brand__name { color: var(--brand-blue-faint); }
  .holder {
    position: absolute; top: 228px; right: 288px; text-align: right;
  }
  .holder__name {
    font-size: 22px; font-weight: 600; color: var(--brand-green); line-height: 1.1;
  }
  .holder__title {
    font-size: 12.5px; color: var(--text-light); margin-top: 4px;
  }
  .divider {
    position: absolute; left: 254px; top: 214px; width: 1px; height: 82px;
    background: var(--divider);
  }
  .contacts {
    position: absolute; left: 274px; top: 213px; list-style: none;
    font-size: 13.5px; line-height: 18px; color: var(--text-light);
  }
  .contacts li { display: flex; gap: 6px; align-items: flex-start; }
  .contacts svg { width: 13px; height: 13px; margin-top: 3px; flex: none; fill: var(--brand-green); }
  .services {
    position: absolute; top: 243px; left: 35px; right: 36px;
    display: flex; justify-content: space-between;
    font-family: "Roboto", Arial, sans-serif; font-weight: 500;
    font-size: 18.5px; letter-spacing: 0.3px;
  }
  .services__item--green { color: var(--brand-green); }
  .services__item--blue { color: var(--brand-blue-bright); }
</style>
</head>
<body>
  <section class="card card--front" aria-label="Business card front">
    <div class="brand">
      <span class="brand__square"></span>
      <span class="brand__name">Quorvel</span>
    </div>
    <div class="card__stripe"></div>
    <div class="card__band"></div>
    <div class="holder">
      <p class="holder__name">Tom Wexley</p>
      <p class="holder__title">Business Manager</p>
    </div>
    <div class="divider"></div>
    <ul class="contacts">
      <li><svg viewBox="0 0 16 16"><path d="M3 1l3 3-2 2c1 2 4 5 6 6l2-2 3 3-2 2C7 15 1 9 1 3z"/></svg>0417586204</li>
      <li><svg viewBox="0 0 16 16"><path d="M1 6l7-5 7 5v8H1z M2.5 7v5.5h11V7L8 11z"/></svg>tom@quorvel.com</li>
      <li><svg viewBox="0 0 16 16"><path d="M8 1a7 7 0 100 14A7 7 0 008 1zm0 1.5c.9 1 1.5 2.6 1.7 4.5H6.3C6.5 5.1 7.1 3.5 8 2.5zM2.6 7a5.5 5.5 0 012.5-3.9C4.6 4.2 4.3 5.5 4.2 7zm0 2h1.6c.1 1.5.4 2.8.9 3.9A5.5 5.5 0 012.6 9zm3.7 0h3.4c-.2 1.9-.8 3.5-1.7 4.5-.9-1-1.5-2.6-1.7-4.5zm5.5 0h1.6a5.5 5.5 0 01-2.5 3.9c.5-1.1.8-2.4.9-3.9zm0-2c-.1-1.5-.4-2.8-.9-3.9A5.5 5.5 0 0113.4 7z"/></svg>quorvelpropertyservices.com.au</li>
      <li><svg viewBox="0 0 16 16"><path d="M8 1L1 8h2v7h4v-4h2v4h4V8h2z"/></svg><span>P.O Box 461 South Melbourne<br>Vic 3090</span></li>
    </ul>
  </section>

  <section class="card card--back" aria-label="Business card back">
    <div class="brand brand--faint" aria-hidden="true">
      <span class="brand__square"></span>
      <span class="brand__name">Quorvel</span>
    </div>
    <div class="card__stripe"></div>
    <div class="card__band"></div>
    <p class="services">
      <span class="services__item--green">CONSTRUCTION</span>
      <span class="services__item--blue">MAINTENANCE</span>
      <span class="services__item--green">REMEDIAL</span>
    </p>
  </section>
</body>
</html>
```